need a clean, modern job advertisement designed for social media (Facebook & Instagram).

The post is to advertise two positions:
• Leading Hand Boilermaker
• Dragline Fitter
We want the design to match our KRT Field Maintenance branding: blue, white, strong, professional, mining-industry style.
What the design should include:
Bold headline: “WE’RE HIRING”
Sub-headline: “Leading Hand Boilermaker & Dragline Fitter”
Key points:
• Bowen Basin based
• Dragline & shovel maintenance
• Great pay + long-term work
• Locally owned & operated
KRT logo placed cleanly
Space for 1–2 images (boilermaking or dragline work)
Design style:
Strong and industrial
Blue/white colour scheme
Easy to read at a glance
Suitable for a square 1080×1080 design

```html
<!DOCTYPE html>
<html lang="en">
<head>
<meta charset="utf-8">
<title>KRT Field Maintenance – We Are Hiring</title>
<link rel="stylesheet" href="https://fonts.googleapis.com/css2?family=Anton&family=Oswald:wght@300;400&family=Poppins:wght@600;700&display=swap">
<style>
  :root {
    --page: #9c9c9c;
    --panel-top: #1f1f20;
    --panel-bottom: #2f3031;
    --white: #ffffff;
    --blue-light: #00b2ff;
    --blue: #0a84ff;
    --ink: #0b1a33;
    --tear: #dcdcdc;
    --photo-a: #1c2340;
    --photo-b: #5a4a6a;
    --photo-c: #c88a4a;
  }
  * { margin: 0; padding: 0; box-sizing: border-box; }
  html, body {
    width: 1200px; height: 899px; overflow: hidden;
    background: var(--page);
  }
  .post {
    position: absolute; left: 255px; top: 104px;
    width: 690px; height: 690px; overflow: hidden;
    background: linear-gradient(180deg, var(--panel-top), var(--panel-bottom));
    color: var(--white);
  }
  .headline-top {
    position: absolute; left: 40px; top: 74px;
    font-family: "Poppins", sans-serif; font-weight: 700;
    font-size: 50px; line-height: 1; letter-spacing: 1px;
    background: linear-gradient(180deg, #ffffff 20%, #9a9a9a 100%);
    -webkit-background-clip: text; background-clip: text; color: transparent;
  }
  .headline-main {
    position: absolute; left: 40px; top: 125px;
    font-family: "Anton", sans-serif; font-size: 120px; line-height: 1;
    letter-spacing: 5px;
    background: linear-gradient(180deg, var(--blue-light), var(--blue));
    -webkit-background-clip: text; background-clip: text; color: transparent;
  }
  .brand {
    position: absolute; left: 440px; top: 135px; width: 236px;
    display: flex; align-items: center; justify-content: center; gap: 10px;
  }
  .brand-dot { width: 22px; height: 22px; border-radius: 50%; background: var(--blue-light); flex: none; }
  .brand-name {
    font-family: "Poppins", sans-serif; font-weight: 700; font-size: 22px;
    line-height: 1.1; color: var(--white);
  }
  .roles {
    position: absolute; left: 42px; top: 258px;
    display: flex; align-items: center; gap: 9px;
  }
  .roles-icon { width: 42px; height: 42px; flex: none; }
  .roles-text {
    font-family: "Poppins", sans-serif; font-weight: 600; font-size: 20.5px;
    line-height: 24px; text-transform: uppercase;
  }
  .photo-band { position: absolute; left: 0; top: 316px; }
  .perks {
    position: absolute; left: 42px; top: 605px;
    display: grid; grid-template-columns: 201px auto; row-gap: 2px;
    font-family: "Oswald", sans-serif; font-weight: 300; font-size: 16.5px; line-height: 24px;
  }
  .perk { display: flex; align-items: center; gap: 4px; white-space: nowrap; }
  .perk svg { flex: none; }
  .apply {
    position: absolute; right: 41px; top: 588px;
    font-family: "Oswald", sans-serif; font-weight: 400; font-size: 26px; line-height: 1;
    letter-spacing: -0.5px;
  }
  .contact {
    position: absolute; left: 450px; top: 622px; width: 214px; height: 34px;
    display: flex; align-items: center; justify-content: flex-end; padding-right: 12px;
    font-family: "Oswald", sans-serif; font-weight: 400; font-size: 23px; color: var(--ink);
  }
  .contact-brush { position: absolute; inset: 0; z-index: 0; }
  .contact span { position: relative; z-index: 1; }
</style>
</head>
<body>
  <main class="post">
    <div class="headline-top">WE ARE</div>
    <div class="headline-main">HIRING!</div>

    <div class="brand">
      <span class="brand-dot"></span>
      <span class="brand-name">KRT Field Maintenance</span>
    </div>

    <div class="roles">
      <svg class="roles-icon" viewBox="0 0 42 42" aria-hidden="true">
        <rect width="42" height="42" rx="5" fill="#0a9bff"/>
        <circle cx="24" cy="17" r="10" fill="none" stroke="#fff" stroke-width="3"/>
        <line x1="17" y1="24" x2="6" y2="37" stroke="#fff" stroke-width="3" stroke-linecap="round"/>
      </svg>
      <p class="roles-text">Leading Hand Boilermaker<br>&amp; Dragline Fitter</p>
    </div>

    <svg class="photo-band" width="690" height="270" viewBox="0 0 690 270">
      <defs>
        <linearGradient id="photoTone" x1="0" y1="0" x2="1" y2="0.3">
          <stop offset="0" stop-color="#1c2340"/>
          <stop offset="0.45" stop-color="#5a4a6a"/>
          <stop offset="0.6" stop-color="#c88a4a"/>
          <stop offset="1" stop-color="#1c2340"/>
        </linearGradient>
      </defs>
      <path fill="#dcdcdc" d="M0 50 L30 42 L60 44 L95 30 L130 26 L170 20 L200 22 L240 26 L280 30 L320 28 L360 34 L400 30 L440 24 L470 18 L500 16 L540 14 L580 12 L620 10 L660 8 L690 2 L690 192 L660 196 L630 208 L600 214 L560 218 L520 226 L480 224 L440 226 L400 218 L360 226 L320 228 L280 228 L240 234 L200 240 L160 244 L120 248 L80 252 L40 250 L0 250 Z"/>
      <path fill="url(#photoTone)" role="img" aria-label="Photo of boilermakers welding in a workshop"
        d="M0 60 L30 52 L60 54 L95 42 L130 36 L170 30 L200 32 L240 36 L280 40 L320 38 L360 42 L400 40 L440 32 L470 26 L500 24 L540 22 L580 20 L620 18 L660 16 L690 12 L690 182 L660 188 L630 198 L600 204 L560 208 L520 214 L480 214 L440 214 L400 208 L360 214 L320 216 L280 218 L240 222 L200 228 L160 232 L120 236 L80 238 L40 240 L0 242 Z"/>
    </svg>

    <div class="perks">
      <div class="perk"><svg width="14" height="16" viewBox="0 0 14 16"><path d="M1 9 L5 14 L13 1" fill="none" stroke="#fff" stroke-width="2"/></svg>Bowen Basin based</div>
      <div class="perk"><svg width="14" height="16" viewBox="0 0 14 16"><path d="M1 9 L5 14 L13 1" fill="none" stroke="#fff" stroke-width="2"/></svg>Great pay + long-term work</div>
      <div class="perk"><svg width="14" height="16" viewBox="0 0 14 16"><path d="M1 9 L5 14 L13 1" fill="none" stroke="#fff" stroke-width="2"/></svg>Dragline &amp; shovel maintenance</div>
      <div class="perk"><svg width="14" height="16" viewBox="0 0 14 16"><path d="M1 9 L5 14 L13 1" fill="none" stroke="#fff" stroke-width="2"/></svg>Locally owned &amp; operated</div>
    </div>

    <div class="apply">APPLY NOW!</div>
    <div class="contact">
      <svg class="contact-brush" viewBox="0 0 214 34" preserveAspectRatio="none" aria-hidden="true">
        <path fill="#0aa0ff" d="M6 4 L200 2 L206 8 L212 12 L204 16 L213 22 L204 28 L196 33 L20 32 L4 30 L10 24 L0 18 L8 12 L2 8 Z"/>
      </svg>
      <span>jobs@krtfield.com.au</span>
    </div>
  </main>
</body>
</html>
```